KA VERLINE

We need a letterhead design for an Image & Etiquette Consultancy company based in Singapore.

The services we provide are Personal Image Consultation, Image & Etiquette Workshop for schools and corporate.

The design should have our corporate colour as seen in the logo files I have uploaded.

Since our company helps clients with their image, the design should be aesthetically very appealing. It should reflect a very classy & elegant feel.

I will print the letterhead using my printer but most of the time will use it to write letters to my clients therefore the format should include MS Word.

```html
<!DOCTYPE html>
<html lang="en">
<head>
<meta charset="utf-8">
<title>KA VERLINE Letterhead</title>
<link rel="stylesheet" href="https://fonts.googleapis.com/css2?family=Source+Sans+3:wght@400;600&display=swap">
<style>
  :root {
    --backdrop: #e4e4e4;
    --paper: #ececee;
    --plum: #2e0f45;
    --gold: #d9ae2c;
    --gold-deep: #c79428;
    --gold-light: #f0e94f;
    --ink: #1c1c1c;
    --body-ink: #2a2a2a;
    --faint: rgba(150,150,150,0.26);
    --sign-tone: #b8c3dc;
  }
  * { margin: 0; padding: 0; box-sizing: border-box; }
  html, body { width: 1113px; height: 1200px; overflow: hidden; }
  body {
    background: var(--backdrop);
    font-family: "Source Sans 3", sans-serif;
    position: relative;
  }
  .letterhead {
    position: absolute;
    left: 95px; top: 62px;
    width: 762px; height: 1076px;
    background: var(--paper);
    box-shadow: 0 1px 4px rgba(0,0,0,0.18);
    overflow: hidden;
  }
  .brand-band {
    position: absolute;
    left: 0; top: 52px;
    width: 390px; height: 83px;
    background: var(--plum);
    display: flex;
    align-items: center;
    padding-left: 33px;
  }
  .brand-name {
    color: var(--gold);
    font-size: 42px;
    font-weight: 400;
    line-height: 1;
    letter-spacing: 9px;
    white-space: nowrap;
  }
  .watermark {
    position: absolute;
    left: 50px; top: 476px;
    color: var(--faint);
    font-size: 80px;
    line-height: 80px;
    letter-spacing: 16px;
    white-space: nowrap;
  }
  .salutation {
    position: absolute;
    left: 107px; top: 248px;
    font-size: 22px;
    color: var(--ink);
  }
  .letter-body {
    position: absolute;
    left: 107px; top: 315px;
    width: 543px;
    font-size: 13.5px;
    line-height: 19.8px;
    color: var(--body-ink);
    text-align: justify;
  }
  .letter-body p + p { margin-top: 19.8px; }
  .closing {
    position: absolute;
    left: 574px; top: 692px;
    font-size: 13px;
    color: var(--body-ink);
  }
  .signature {
    position: absolute;
    left: 480px; top: 722px;
    width: 160px; height: 66px;
    background: var(--sign-tone);
    opacity: 0.5;
    border-radius: 4px;
  }
  .contact-band {
    position: absolute;
    left: 0; top: 1011px;
    width: 762px; height: 38px;
    background: linear-gradient(90deg, var(--gold-deep) 0%, var(--gold-light) 60%, var(--gold-deep) 100%);
    display: flex;
    justify-content: space-between;
    align-items: center;
    padding: 0 52px 0 53px;
    font-size: 14.5px;
    color: var(--ink);
    letter-spacing: 0.3px;
  }
</style>
</head>
<body>
  <main class="letterhead">
    <header class="brand-band">
      <div class="brand-name">KA VERLINE</div>
    </header>

    <div class="watermark" aria-hidden="true">KA VERLINE</div>

    <p class="salutation">Dear Ms. Tan,</p>

    <section class="letter-body">
      <p>Lorem ipsum dolor sit amet, consectetur adipiscing elit. Donec orci purus, luctus vitae dignissim eu, iaculis sed purus. Vivamus faucibus, ipsum nec aliquet viverra, leo mauris condimentum ligula, sit amet sagittis enim ligula quis arcu. Nam egestas tortor id nisi porttitor mattis. In tortor ante, ultricies in suscipit a, tempus non massa. Vivamus et auctor mi. Fusce vel massa nulla. Phasellus nec eros mauris, et scelerisque orci.</p>
      <p>Donec malesuada orci vitae nulla accumsan porta a id massa. Quisque accumsan iaculis magna sit amet fringilla. Maecenas consequat, magna eget tincidunt semper, odio nibh rutrum mi, id feugiat ante nisi eu risus. Vestibulum nunc orci, rhoncus a placerat in, ultricies in mi. Cras mattis varius eros, vel fringilla nisi suscipit eget. Quisque scelerisque sagittis nulla at porttitor.</p>
      <p>Sed id augue vitae urna euismod commodo aliquet a quam. Pellentesque arcu velit, cursus et malesuada ut, consequat et diam. Nullam erat sem, rhoncus id ullamcorper vitae, rhoncus et arcu. In ultricies ultricies nulla, ut rutrum nisi iaculis at. Donec eu magna a metus ornare faucibus. Fusce aliquet faucibus ultricies. Morbi semper, est id tincidunt gravida, sem arcu adipiscing lacus, ac bibendum nulla leo eu purus. Quisque nec diam sed risus consectetur a ccumsan quis quis nibh. Vestibulum id purus lorem.</p>
    </section>

    <p class="closing">Sincerely,</p>
    <div class="signature" role="img" aria-label="Handwritten signature of Lena Marsh"></div>

    <footer class="contact-band">
      <span>Tell: 6123 4567</span>
      <span>Web: kaverline.com</span>
      <span>Email: hello@kaverline.com</span>
    </footer>
  </main>
</body>
</html>
```